Simple+Professional tech feel + warm and friendly box design for pet test kit

Project Name: 10-Minute Canine & Feline Rapid Test Kit Packaging Design
Target Brand Reference: VETRALUX (South Korea) styles
Design Style Direction: Professional tech feel + warm and friendly
Professionalism (Professional): Clear typography and distinct information hierarchy to reflect the product’s scientific rigor and accuracy.
Technological: Reflected through clean graphics and a minimalist layout.
Friendly: Utilise soft, warm colour combinations to convey care for pets and well-wishes for their health.
International: The design should align with mainstream aesthetics and avoid cultural ambiguities.

Target Market(s)
European Union and the United States
Industry/Entity Type
Veterinary Medical
Look and feel
Each slider illustrates characteristics of the customer's brand and the style your logo design should communicate.

```html
<!DOCTYPE html>
<html lang="en">
<head>
<meta charset="utf-8">
<title>ClaraPaw Rapid Test Kit – Carton Dieline</title>
<link rel="stylesheet" href="https://fonts.googleapis.com/css2?family=Arimo:wght@700&family=Hind:wght@500;600&family=Open+Sans:wght@400;600&display=swap">
<style>
  :root{
    --paper:#ffffff;
    --cream:#fdf6ea;
    --peach:#fbc173;
    --orange:#f59a34;
    --ink:#1c1c1c;
    --ink-soft:#2e2e2e;
    --cut:#111111;
    --crease:#1aa3dd;
    --shadow:#9b9b9b;
    --white:#ffffff;
  }
  html,body{margin:0;padding:0;overflow:hidden;background:var(--paper);}
  .sheet{width:1200px;height:1200px;position:relative;overflow:hidden;background:var(--paper);}
  .sheet svg{position:absolute;left:0;top:0;}
  .logo{font-family:"Arimo",Arial,sans-serif;font-weight:700;fill:var(--ink);}
  .tm{font-family:"Arimo",Arial,sans-serif;font-weight:400;fill:var(--ink);}
  .title{font-family:"Hind",sans-serif;font-weight:600;fill:var(--ink-soft);font-size:23px;}
  .subtitle{font-family:"Open Sans",sans-serif;fill:var(--ink-soft);font-size:13px;}
  .count{font-family:"Open Sans",sans-serif;font-weight:600;fill:var(--ink);font-size:15px;}
  .maker{font-family:"Open Sans",sans-serif;font-weight:600;fill:var(--white);font-size:34px;}
  .tagline{font-family:"Hind",sans-serif;font-weight:500;fill:var(--ink-soft);font-size:13.5px;}
  .side-white{font-family:"Hind",sans-serif;font-weight:500;fill:var(--white);font-size:11px;}
  .micro{font-family:"Open Sans",sans-serif;fill:var(--white);font-size:6px;letter-spacing:.3px;}
  .story{font-family:"Open Sans",sans-serif;fill:var(--white);font-size:7.4px;}
  .spec{font-family:"Open Sans",sans-serif;fill:var(--ink);font-size:19px;}
  .legend{font-family:"Open Sans",sans-serif;fill:var(--ink);font-size:15px;letter-spacing:1px;}
</style>
</head>
<body>
<div class="sheet">
<svg width="1200" height="1200" viewBox="0 0 1200 1200">
  <defs>
    <path id="dieline-outline" d="M34,945 V411 Q34,383 62,383 H384 Q412,383 412,411 V692 L421,680 V596 Q421,580 437,580 H564 Q578,580 579,594 L587,672 L593,680 L595,692 H974 L975,680 L980,674 L988,594 Q990,580 1004,580 H1150 V680 L1157,692 L1180,702 V935 L1157,945 V1099 Q1157,1118 1138,1118 H1031 Q1011,1114 1011,1093 L1031,1039 L974,945 V1112 Q974,1135 951,1135 H903 Q880,1135 880,1112 V1071 H689 V1112 Q689,1135 666,1135 H618 Q595,1135 595,1112 V945 L539,1039 L559,1093 Q561,1118 536,1118 H435 Q412,1118 412,1095 V945 L315,1071 V1110 Q315,1135 290,1135 H156 Q131,1135 131,1110 V1071 Z"/>
    <linearGradient id="side-band" x1="0" y1="0" x2="0" y2="1">
      <stop offset="0" stop-color="#fbc173"/>
      <stop offset="1" stop-color="#f59a34"/>
    </linearGradient>
    <linearGradient id="art-tone" x1="0" y1="0" x2="1" y2="1">
      <stop offset="0" stop-color="#f3a94f"/>
      <stop offset="1" stop-color="#f39a35"/>
    </linearGradient>
    <g id="face-band">
      <rect x="0" y="0" width="379" height="253" fill="var(--orange)"/>
      <rect x="0" y="0" width="379" height="62" fill="var(--peach)"/>
      <path d="M0,67 H138 C154,67 160,55 178,55 H379 V207 H222 C202,207 194,195 176,195 H0 Z" fill="var(--cream)"/>
    </g>
  </defs>

  <!-- spec label -->
  <text class="spec" x="19" y="38">135x65x90mm</text>

  <!-- drop shadow & carton body -->
  <use href="#dieline-outline" transform="translate(20,20)" fill="var(--shadow)"/>
  <use href="#dieline-outline" fill="var(--cream)"/>

  <!-- back face band -->
  <use href="#face-band" x="34" y="692"/>
  <!-- front face band -->
  <use href="#face-band" x="595" y="692"/>
  <!-- side panel bands -->
  <rect x="412" y="747" width="183" height="152" fill="url(#side-band)"/>
  <rect x="974" y="747" width="183" height="152" fill="url(#side-band)"/>
  <!-- glue tab -->
  <path d="M1157,692 L1180,702 V747 H1157 Z" fill="var(--peach)"/>
  <path d="M1157,899 H1180 V935 L1157,945 Z" fill="var(--orange)"/>

  <!-- cut line -->
  <use href="#dieline-outline" fill="none" stroke="var(--cut)" stroke-width="1.6"/>

  <!-- crease lines -->
  <g stroke="var(--crease)" stroke-width="1.5" fill="none">
    <line x1="34" y1="439" x2="412" y2="439"/>
    <line x1="34" y1="692" x2="1157" y2="692"/>
    <line x1="34" y1="945" x2="1157" y2="945"/>
    <line x1="412" y1="692" x2="412" y2="945"/>
    <line x1="595" y1="692" x2="595" y2="945"/>
    <line x1="974" y1="692" x2="974" y2="945"/>
    <line x1="1157" y1="692" x2="1157" y2="945"/>
  </g>

  <!-- top flap product name -->
  <text class="logo" x="106" y="584" font-size="54">ClaraPaw<tspan class="tm" font-size="17" dy="-26">TM</tspan></text>

  <!-- back face content -->
  <g class="face-content" transform="translate(34,692)">
    <text class="logo" x="23" y="43" font-size="34">ClaraPaw<tspan class="tm" font-size="11" dy="-16">TM</tspan></text>
    <text class="title" x="25" y="95">10-Minute</text>
    <text class="title" x="25" y="121">Canine &amp; Feline</text>
    <text class="title" x="25" y="147">Rapid Test Kit</text>
    <text class="subtitle" x="24" y="173">For Dogs and Cats</text>
    <rect x="202" y="66" width="152" height="106" rx="14" fill="url(#art-tone)" role="img" aria-label="Illustration of a dog and a cat in orange silhouette"/>
    <text class="count" x="278" y="190" text-anchor="middle">5 Tests/Kit</text>
    <text class="maker" x="25" y="229">Orvella</text>
  </g>

  <!-- front face content -->
  <g class="face-content" transform="translate(595,692)">
    <text class="logo" x="25" y="43" font-size="34">ClaraPaw<tspan class="tm" font-size="11" dy="-16">TM</tspan></text>
    <text class="title" x="27" y="95">10-Minute</text>
    <text class="title" x="27" y="121">Canine &amp; Feline</text>
    <text class="title" x="27" y="147">Rapid Test Kit</text>
    <text class="subtitle" x="26" y="173">For Dogs and Cats</text>
    <rect x="204" y="66" width="152" height="106" rx="14" fill="url(#art-tone)" role="img" aria-label="Illustration of a dog and a cat in orange silhouette"/>
    <text class="count" x="280" y="190" text-anchor="middle">5 Tests/Kit</text>
    <text class="maker" x="27" y="229">Orvella</text>
  </g>

  <!-- left side panel -->
  <g class="side-info">
    <text class="tagline" x="433" y="771">A Clear View into</text>
    <text class="tagline" x="433" y="788">Pet Health</text>
    <line x1="433" y1="795" x2="526" y2="795" stroke="var(--white)" stroke-width="1.2"/>
    <text class="side-white" x="433" y="807">Made by Orvella</text>
    <text class="micro" x="433" y="836">Orvella Biotech Limited</text>
    <text class="micro" x="434" y="844">Web:www.orvella-bio.example</text>
    <text class="micro" x="434" y="852">E-mail:hello@orvella-bio.example</text>
    <text class="micro" x="433" y="875">(For accurate results, please read the</text>
    <text class="micro" x="433" y="884">instructions carefully before use)</text>
  </g>

  <!-- right side panel -->
  <g class="brand-story" text-anchor="middle">
    <text class="story" x="1066" y="796">ClaraPaw is made by Orvella, our</text>
    <text class="story" x="1066" y="806">name joins 'Orva' for innovation</text>
    <text class="story" x="1066" y="816">with "Vellis" from philosophy,</text>
    <text class="story" x="1066" y="826">representing both intelligent efficacy in</text>
    <text class="story" x="1066" y="836">our science and reverence for the</text>
    <text class="story" x="1066" y="846">spirit of life ('Orva Vellis')</text>
    <text class="story" x="1066" y="856">in all creatures</text>
  </g>

  <!-- legend -->
  <text class="legend" x="20" y="1182">CUTTING AREA</text>
  <rect x="154" y="1171" width="48" height="11" rx="3" fill="var(--cut)"/>
  <text class="legend" x="261" y="1182">CREASING AREA</text>
  <rect x="410" y="1171" width="48" height="11" rx="3" fill="var(--crease)"/>
</svg>
</div>
</body>
</html>
```